Supplement Label Design for “Kept 2 Thrive Core” – Premium Bilingual Supplement

Kept 2 Thrive is a premium, individually crafted supplement brand specializing in targeted solutions for specific health issues.
We are launching our first product: Kept 2 Thrive Core — a high-quality blend focused on stomach and digestive health.
Primary goals:
• Reduce symptoms caused by Helicobacter pylori (acidity after meals, stomach pain and discomfort)
• Support repair of the gut lining
• Strengthen the local immune system in the digestive tract
Label Requirements:
• Premium, elegant, and modern design (high-end supplement feel)
• Dominant yellow / golden color scheme for this Core blend (future blends will have different signature colors, e.g. red for Pulse blend)
• Include a stylized, positive illustration of a healthy stomach on the label
• Fully bilingual — English and Bulgarian if possible (both languages must be clearly visible and well balanced)
• Logo is already uploaded
• Must feel trustworthy, clean, and professional
We need both front and back label designs suitable for a standard supplement bottle.

Target Market(s)

The target is health-conscious individuals, particularly my personal patients who suffer from stomach issues, H. pylori related symptoms, and digestive discomfort. People looking for premium, science-oriented natural supplements.

Industry/Entity Type

Functional medicine

Font styles to use
Sans Serif

Colors
FFC000
F8CF3A
FAE287
FDF2CF
FEFAEE

Requirements
Must have
• • Premium and luxurious look • Dominant yellow/golden color palette • Stylized healthy stomach illustration • Bilingual (English + Bulgarian) • Clean, minimalist yet elegant design • Professional and trustworthy appearance • Include the “Kept 2 Thrive” logo
Nice to have
• • Subtle visual indication of positive effect on the stomach/gut • Elegant iconography or subtle patterns related to health and nature • Easy-to-read hierarchy for important information • Modern minimalist style with premium finishing feel
Should not have
• Cheap or generic look • Overly cartoonish or childish stomach drawing • Too much clutter or overcrowded desig

```html
<!DOCTYPE html>
<html lang="en">
<head>
<meta charset="utf-8">
<title>Kept 2 Thrive Core – label set</title>
<link rel="stylesheet" href="https://fonts.googleapis.com/css2?family=Cinzel:wght@400;600;700&family=Montserrat:wght@400;500;600;700;800&display=swap">
<style>
  :root {
    --gold-deep: #c8921a;
    --gold: #e2aa2c;
    --gold-bright: #ffc000;
    --gold-soft: #f8cf3a;
    --gold-pale: #fae287;
    --cream: #fdf2cf;
    --ivory: #fefaee;
    --green: #0e7a3c;
    --ink: #2b2b2b;
    --canvas: #f2f2ef;
    --serif: 'Cinzel', Georgia, serif;
    --sans: 'Montserrat', Arial, sans-serif;
  }
  * { box-sizing: border-box; margin: 0; padding: 0; }
  html, body { width: 1200px; height: 360px; overflow: hidden; background: var(--canvas); }
  .label-sheet { position: relative; width: 1200px; height: 360px; }

  .front-label, .back-label {
    position: absolute; top: 12px; width: 160px; height: 334px;
    background: #fff; overflow: hidden;
    box-shadow: 0 0 2px rgba(0,0,0,.12);
  }
  .front-backdrop { position: absolute; inset: 0; width: 160px; height: 334px; }

  /* brand name: one colour, one weight, single plain circle beside it */
  .brand-name {
    position: absolute; top: 14px; left: 0; right: 0;
    display: flex; align-items: center; justify-content: center; gap: 4px;
    font-family: var(--sans); font-weight: 500; font-size: 8px; letter-spacing: 1.4px;
    text-transform: uppercase; color: var(--gold);
  }
  .brand-name .brand-dot { width: 6px; height: 6px; border-radius: 50%; background: var(--gold); }

  .tagline {
    position: absolute; top: 45px; left: 0; right: 0; text-align: center;
    font-family: var(--serif); font-weight: 600; font-size: 12.5px; color: var(--green); letter-spacing: .3px;
  }
  .product-name {
    position: absolute; top: 58px; left: 0; right: 0; text-align: center;
    font-family: var(--serif); font-weight: 700; font-size: 33px; line-height: 1;
    color: var(--gold); letter-spacing: 1px;
  }
  .desc-en, .desc-bg {
    position: absolute; text-align: center;
    font-family: var(--sans); font-size: 3.3px; color: #555;
  }
  .desc-en { top: 94px; left: 30px; right: 30px; line-height: 5.6px; }
  .desc-bg { top: 241px; left: 22px; right: 22px; line-height: 5.1px; }

  .hero-art {
    position: absolute; top: 124px; left: 32px; width: 96px; height: 96px; border-radius: 46% 54% 50% 50%;
    background: radial-gradient(circle at 42% 38%, #fff4c4 0%, var(--gold-soft) 35%, var(--gold) 70%, rgba(200,146,26,0) 72%);
  }

  .product-name-bg {
    position: absolute; top: 222px; left: 0; right: 0; text-align: center;
    font-family: var(--sans); font-weight: 800; font-size: 14px; line-height: 16px; color: var(--green); letter-spacing: .2px;
  }

  .benefit-row {
    position: absolute; top: 282px; left: 4px; right: 4px;
    display: grid; grid-template-columns: repeat(4, 1fr);
  }
  .benefit { text-align: center; color: #fff; font-family: var(--sans); }
  .benefit-icon {
    width: 16px; height: 16px; margin: 0 auto 4px; border-radius: 50%;
    background: #fff; border: 1.5px solid var(--gold-soft);
    display: flex; align-items: center; justify-content: center;
  }
  .benefit-icon svg { width: 9px; height: 9px; }
  .benefit-en { font-size: 2.6px; font-weight: 600; line-height: 4px; }
  .benefit-bg { font-size: 2.6px; font-weight: 600; line-height: 3.4px; margin-top: 4px; }

  .footer-bar {
    position: absolute; bottom: 0; left: 0; right: 0; height: 11px; background: var(--green);
    display: flex; align-items: center; justify-content: space-between; padding: 0 6px;
    color: #fff; font-family: var(--sans); font-size: 3.2px; font-weight: 600;
  }
  .footer-bar b { font-family: var(--serif); font-size: 3.6px; letter-spacing: .2px; }

  /* back label */
  .back-label { font-family: var(--sans); color: var(--ink); }
  .back-block { position: absolute; left: 5px; right: 5px; overflow: hidden; }
  .back-heading { font-size: 4.6px; line-height: 6px; font-weight: 700; }
  .back-heading.small { font-size: 3.4px; line-height: 5px; }
  .back-text { font-size: 2.4px; line-height: 5px; color: #444; text-align: justify; }
  .back-text.tight { line-height: 4.2px; }
  .compo-table {
    position: absolute; top: 84px; left: 9px; right: 9px; height: 126px;
    border: .6px solid var(--gold-soft);
    display: grid; grid-template-columns: 1.45fr 1fr 1fr; grid-template-rows: 16px repeat(7, 1fr);
  }
  .compo-table > div { font-size: 2.9px; line-height: 4px; padding: 3px 3px 0; border-top: .4px solid #e6dcc0; color: #444; }
  .compo-table .th { background: var(--gold-soft); color: #5a3e00; font-family: var(--serif); font-weight: 600; border-top: none; font-size: 3.4px; padding-top: 3.5px; }
  .compo-table .num { border-left: .4px solid #e6dcc0; }
  .two-col { display: grid; grid-template-columns: 1fr 1fr; gap: 8px; }
  .dosage-band {
    position: absolute; top: 238px; left: 0; right: 0; height: 13px;
    padding: 2.4px 5px 0; text-align: center;
    background: linear-gradient(90deg, var(--gold-soft), var(--gold-bright), var(--gold-soft));
    font-size: 2.6px; line-height: 4px; color: #3a2a00;
  }
  .dosage-band b { font-weight: 700; }
  .lot-band {
    position: absolute; left: 0; right: 0; bottom: 0; height: 10px;
    background: linear-gradient(90deg, var(--gold-pale), var(--gold-soft));
    display: flex; align-items: center; justify-content: space-between; padding: 0 14px;
    font-size: 3.2px; font-weight: 600;
  }
</style>
</head>
<body>
<main class="label-sheet">

<svg width="0" height="0" style="position:absolute" aria-hidden="true">
  <defs><linearGradient id="goldFill" x1="0" y1="0" x2="0" y2="1"><stop offset="0" stop-color="#f6cd55"/><stop offset="1" stop-color="#d99a1c"/></linearGradient></defs>
</svg>

<section class="front-label" style="left:13px">
  <svg class="front-backdrop" viewBox="0 0 160 334" aria-hidden="true">
    <path d="M160 82 C120 150 50 130 0 170 V334 H160 Z" fill="var(--ivory)"/>
    <path d="M160 82 C120 150 50 130 0 170" fill="none" stroke="var(--gold-pale)" stroke-width="1.6"/>
    <path d="M0 277 C45 262 110 282 160 266 V334 H0 Z" fill="url(#goldFill)"/>
  </svg>
  <div class="brand-name"><span class="brand-dot"></span><span>Kept 2 Thrive</span></div>
  <div class="tagline">KEPT 2 THRIVE</div>
  <div class="product-name">CORE</div>
  <p class="desc-en">Food supplement with vegetable extracts of Licorice, Red elm, Althaea, Aloe vera, with Mastics of Chios, N-acetylcysteine and Lactoferrin.</p>
  <div class="hero-art" role="img" aria-label="Glowing golden stomach illustration"></div>
  <h2 class="product-name-bg">КЕПТ ТУ ТРАЙВ КОР</h2>
  <p class="desc-bg">Хранителна добавка с растителни екстракти от Женско биле, Червен бряст, Алтея, Алое вера, с Мастика от Хиос, N-ацетилцистеин и Лактоферин.</p>
  <div class="benefit-row">
    <div class="benefit"><div class="benefit-icon"><svg viewBox="0 0 10 10"><circle cx="5" cy="5" r="3" fill="none" stroke="#0e7a3c" stroke-width="1.2"/></svg></div><div class="benefit-en">DIGESTIVE COMFORT</div><div class="benefit-bg">КОМФОРТ ПРИ ХРАНОСМИЛАНЕ</div></div>
    <div class="benefit"><div class="benefit-icon"><svg viewBox="0 0 10 10"><path d="M2 5 L4 7 L8 3" fill="none" stroke="#0e7a3c" stroke-width="1.3"/></svg></div><div class="benefit-en">GUT LINING SUPPORT</div><div class="benefit-bg">ПОДПОМАГА ЛИГАВИЦАТА</div></div>
    <div class="benefit"><div class="benefit-icon"><svg viewBox="0 0 10 10"><circle cx="5" cy="5" r="1.6" fill="#0e7a3c"/><circle cx="5" cy="5" r="3.6" fill="none" stroke="#0e7a3c" stroke-width=".8" stroke-dasharray="1 1"/></svg></div><div class="benefit-en">IMMUNE SUPPORT</div><div class="benefit-bg">ПОДКРЕПА НА ИМУНИТЕТА</div></div>
    <div class="benefit"><div class="benefit-icon"><svg viewBox="0 0 10 10"><path d="M5 8 V3 M5 5 C3 5 2.5 3.5 2.5 2.5 C4 2.5 5 3.5 5 5 C5 3.5 6 2.5 7.5 2.5 C7.5 3.5 7 5 5 5" fill="none" stroke="#0e7a3c" stroke-width=".9"/></svg></div><div class="benefit-en">NATURAL INGREDIENTS</div><div class="benefit-bg">НАТУРАЛНИ СЪСТАВКИ</div></div>
  </div>
  <footer class="footer-bar"><span><b>DIETARY SUPPLEMENT</b> | ХРАНИТЕЛНА ДОБАВКА</span><span><b>60 CAPSULES</b> | КАПСУЛИ</span></footer>
</section>

<section class="front-label" style="left:182px">
  <svg class="front-backdrop" viewBox="0 0 160 334" aria-hidden="true">
    <path d="M160 82 C120 150 50 130 0 170 V334 H160 Z" fill="var(--ivory)"/>
    <path d="M160 82 C120 150 50 130 0 170" fill="none" stroke="var(--gold-pale)" stroke-width="1.6"/>
    <path d="M0 277 C45 262 110 282 160 266 V334 H0 Z" fill="url(#goldFill)"/>
  </svg>
  <div class="brand-name"><span class="brand-dot"></span><span>Kept 2 Thrive</span></div>
  <div class="tagline">KEPT 2 THRIVE</div>
  <div class="product-name">CORE</div>
  <p class="desc-en">Food supplement with vegetable extracts of Licorice, Red elm, Althaea, Aloe vera, with Mastics of Chios, N-acetylcysteine and Lactoferrin.</p>
  <div class="hero-art" role="img" aria-label="Golden stomach illustration"></div>
  <h2 class="product-name-bg">КЕПТ ТУ ТРАЙВ КОР</h2>
  <p class="desc-bg">Хранителна добавка с растителни екстракти от Женско биле, Червен бряст, Алтея, Алое вера, с Мастика от Хиос, N-ацетилцистеин и Лактоферин.</p>
  <div class="benefit-row">
    <div class="benefit"><div class="benefit-icon"><svg viewBox="0 0 10 10"><circle cx="5" cy="5" r="3" fill="none" stroke="#0e7a3c" stroke-width="1.2"/></svg></div><div class="benefit-en">DIGESTIVE COMFORT</div><div class="benefit-bg">КОМФОРТ ПРИ ХРАНОСМИЛАНЕ</div></div>
    <div class="benefit"><div class="benefit-icon"><svg viewBox="0 0 10 10"><path d="M2 5 L4 7 L8 3" fill="none" stroke="#0e7a3c" stroke-width="1.3"/></svg></div><div class="benefit-en">GUT LINING SUPPORT</div><div class="benefit-bg">ПОДПОМАГА ЛИГАВИЦАТА</div></div>
    <div class="benefit"><div class="benefit-icon"><svg viewBox="0 0 10 10"><circle cx="5" cy="5" r="1.6" fill="#0e7a3c"/><circle cx="5" cy="5" r="3.6" fill="none" stroke="#0e7a3c" stroke-width=".8" stroke-dasharray="1 1"/></svg></div><div class="benefit-en">IMMUNE SUPPORT</div><div class="benefit-bg">ПОДКРЕПА НА ИМУНИТЕТА</div></div>
    <div class="benefit"><div class="benefit-icon"><svg viewBox="0 0 10 10"><path d="M5 8 V3 M5 5 C3 5 2.5 3.5 2.5 2.5 C4 2.5 5 3.5 5 5 C5 3.5 6 2.5 7.5 2.5 C7.5 3.5 7 5 5 5" fill="none" stroke="#0e7a3c" stroke-width=".9"/></svg></div><div class="benefit-en">NATURAL INGREDIENTS</div><div class="benefit-bg">НАТУРАЛНИ СЪСТАВКИ</div></div>
  </div>
  <footer class="footer-bar"><span><b>DIETARY SUPPLEMENT</b> | ХРАНИТЕЛНА ДОБАВКА</span><span><b>60 CAPSULES</b> | КАПСУЛИ</span></footer>
</section>

<section class="front-label" style="left:351px">
  <svg class="front-backdrop" viewBox="0 0 160 334" aria-hidden="true">
    <path d="M160 82 C120 150 50 130 0 170 V334 H160 Z" fill="var(--ivory)"/>
    <path d="M160 82 C120 150 50 130 0 170" fill="none" stroke="var(--gold-pale)" stroke-width="1.6"/>
    <path d="M0 277 C45 262 110 282 160 266 V334 H0 Z" fill="url(#goldFill)"/>
  </svg>
  <div class="brand-name"><span class="brand-dot"></span><span>Kept 2 Thrive</span></div>
  <div class="tagline">KEPT 2 THRIVE</div>
  <div class="product-name">CORE</div>
  <p class="desc-en">Food supplement with vegetable extracts of Licorice, Red elm, Althaea, Aloe vera, with Mastics of Chios, N-acetylcysteine and Lactoferrin.</p>
  <div class="hero-art" role="img" aria-label="Golden intestines illustration"></div>
  <h2 class="product-name-bg">КЕПТ ТУ ТРАЙВ КОР</h2>
  <p class="desc-bg">Хранителна добавка с растителни екстракти от Женско биле, Червен бряст, Алтея, Алое вера, с Мастика от Хиос, N-ацетилцистеин и Лактоферин.</p>
  <div class="benefit-row">
    <div class="benefit"><div class="benefit-icon"><svg viewBox="0 0 10 10"><circle cx="5" cy="5" r="3" fill="none" stroke="#0e7a3c" stroke-width="1.2"/></svg></div><div class="benefit-en">DIGESTIVE COMFORT</div><div class="benefit-bg">КОМФОРТ ПРИ ХРАНОСМИЛАНЕ</div></div>
    <div class="benefit"><div class="benefit-icon"><svg viewBox="0 0 10 10"><path d="M2 5 L4 7 L8 3" fill="none" stroke="#0e7a3c" stroke-width="1.3"/></svg></div><div class="benefit-en">GUT LINING SUPPORT</div><div class="benefit-bg">ПОДПОМАГА ЛИГАВИЦАТА</div></div>
    <div class="benefit"><div class="benefit-icon"><svg viewBox="0 0 10 10"><circle cx="5" cy="5" r="1.6" fill="#0e7a3c"/><circle cx="5" cy="5" r="3.6" fill="none" stroke="#0e7a3c" stroke-width=".8" stroke-dasharray="1 1"/></svg></div><div class="benefit-en">IMMUNE SUPPORT</div><div class="benefit-bg">ПОДКРЕПА НА ИМУНИТЕТА</div></div>
    <div class="benefit"><div class="benefit-icon"><svg viewBox="0 0 10 10"><path d="M5 8 V3 M5 5 C3 5 2.5 3.5 2.5 2.5 C4 2.5 5 3.5 5 5 C5 3.5 6 2.5 7.5 2.5 C7.5 3.5 7 5 5 5" fill="none" stroke="#0e7a3c" stroke-width=".9"/></svg></div><div class="benefit-en">NATURAL INGREDIENTS</div><div class="benefit-bg">НАТУРАЛНИ СЪСТАВКИ</div></div>
  </div>
  <footer class="footer-bar"><span><b>DIETARY SUPPLEMENT</b> | ХРАНИТЕЛНА ДОБАВКА</span><span><b>60 CAPSULES</b> | КАПСУЛИ</span></footer>
</section>

<section class="front-label" style="left:520px">
  <svg class="front-backdrop" viewBox="0 0 160 334" aria-hidden="true">
    <path d="M160 82 C120 150 50 130 0 170 V334 H160 Z" fill="var(--ivory)"/>
    <path d="M160 82 C120 150 50 130 0 170" fill="none" stroke="var(--gold-pale)" stroke-width="1.6"/>
    <path d="M0 277 C45 262 110 282 160 266 V334 H0 Z" fill="url(#goldFill)"/>
  </svg>
  <div class="brand-name"><span class="brand-dot"></span><span>Kept 2 Thrive</span></div>
  <div class="tagline">KEPT 2 THRIVE</div>
  <div class="product-name">CORE</div>
  <p class="desc-en">Food supplement with vegetable extracts of Licorice, Red elm, Althaea, Aloe vera, with Mastics of Chios, N-acetylcysteine and Lactoferrin.</p>
  <div class="hero-art" role="img" aria-label="Golden stomach illustration, side view"></div>
  <h2 class="product-name-bg">КЕПТ ТУ ТРАЙВ КОР</h2>
  <p class="desc-bg">Хранителна добавка с растителни екстракти от Женско биле, Червен бряст, Алтея, Алое вера, с Мастика от Хиос, N-ацетилцистеин и Лактоферин.</p>
  <div class="benefit-row">
    <div class="benefit"><div class="benefit-icon"><svg viewBox="0 0 10 10"><circle cx="5" cy="5" r="3" fill="none" stroke="#0e7a3c" stroke-width="1.2"/></svg></div><div class="benefit-en">DIGESTIVE COMFORT</div><div class="benefit-bg">КОМФОРТ ПРИ ХРАНОСМИЛАНЕ</div></div>
    <div class="benefit"><div class="benefit-icon"><svg viewBox="0 0 10 10"><path d="M2 5 L4 7 L8 3" fill="none" stroke="#0e7a3c" stroke-width="1.3"/></svg></div><div class="benefit-en">GUT LINING SUPPORT</div><div class="benefit-bg">ПОДПОМАГА ЛИГАВИЦАТА</div></div>
    <div class="benefit"><div class="benefit-icon"><svg viewBox="0 0 10 10"><circle cx="5" cy="5" r="1.6" fill="#0e7a3c"/><circle cx="5" cy="5" r="3.6" fill="none" stroke="#0e7a3c" stroke-width=".8" stroke-dasharray="1 1"/></svg></div><div class="benefit-en">IMMUNE SUPPORT</div><div class="benefit-bg">ПОДКРЕПА НА ИМУНИТЕТА</div></div>
    <div class="benefit"><div class="benefit-icon"><svg viewBox="0 0 10 10"><path d="M5 8 V3 M5 5 C3 5 2.5 3.5 2.5 2.5 C4 2.5 5 3.5 5 5 C5 3.5 6 2.5 7.5 2.5 C7.5 3.5 7 5 5 5" fill="none" stroke="#0e7a3c" stroke-width=".9"/></svg></div><div class="benefit-en">NATURAL INGREDIENTS</div><div class="benefit-bg">НАТУРАЛНИ СЪСТАВКИ</div></div>
  </div>
  <footer class="footer-bar"><span><b>DIETARY SUPPLEMENT</b> | ХРАНИТЕЛНА ДОБАВКА</span><span><b>60 CAPSULES</b> | КАПСУЛИ</span></footer>
</section>

<section class="front-label" style="left:689px">
  <svg class="front-backdrop" viewBox="0 0 160 334" aria-hidden="true">
    <path d="M160 82 C120 150 50 130 0 170 V334 H160 Z" fill="var(--ivory)"/>
    <path d="M160 82 C120 150 50 130 0 170" fill="none" stroke="var(--gold-pale)" stroke-width="1.6"/>
    <path d="M0 277 C45 262 110 282 160 266 V334 H0 Z" fill="url(#goldFill)"/>
  </svg>
  <div class="brand-name"><span class="brand-dot"></span><span>Kept 2 Thrive</span></div>
  <div class="tagline">KEPT 2 THRIVE</div>
  <div class="product-name">CORE</div>
  <p class="desc-en">Food supplement with vegetable extracts of Licorice, Red elm, Althaea, Aloe vera, with Mastics of Chios, N-acetylcysteine and Lactoferrin.</p>
  <div class="hero-art" role="img" aria-label="Golden digestive tract illustration"></div>
  <h2 class="product-name-bg">КЕПТ ТУ ТРАЙВ КОР</h2>
  <p class="desc-bg">Хранителна добавка с растителни екстракти от Женско биле, Червен бряст, Алтея, Алое вера, с Мастика от Хиос, N-ацетилцистеин и Лактоферин.</p>
  <div class="benefit-row">
    <div class="benefit"><div class="benefit-icon"><svg viewBox="0 0 10 10"><circle cx="5" cy="5" r="3" fill="none" stroke="#0e7a3c" stroke-width="1.2"/></svg></div><div class="benefit-en">DIGESTIVE COMFORT</div><div class="benefit-bg">КОМФОРТ ПРИ ХРАНОСМИЛАНЕ</div></div>
    <div class="benefit"><div class="benefit-icon"><svg viewBox="0 0 10 10"><path d="M2 5 L4 7 L8 3" fill="none" stroke="#0e7a3c" stroke-width="1.3"/></svg></div><div class="benefit-en">GUT LINING SUPPORT</div><div class="benefit-bg">ПОДПОМАГА ЛИГАВИЦАТА</div></div>
    <div class="benefit"><div class="benefit-icon"><svg viewBox="0 0 10 10"><circle cx="5" cy="5" r="1.6" fill="#0e7a3c"/><circle cx="5" cy="5" r="3.6" fill="none" stroke="#0e7a3c" stroke-width=".8" stroke-dasharray="1 1"/></svg></div><div class="benefit-en">IMMUNE SUPPORT</div><div class="benefit-bg">ПОДКРЕПА НА ИМУНИТЕТА</div></div>
    <div class="benefit"><div class="benefit-icon"><svg viewBox="0 0 10 10"><path d="M5 8 V3 M5 5 C3 5 2.5 3.5 2.5 2.5 C4 2.5 5 3.5 5 5 C5 3.5 6 2.5 7.5 2.5 C7.5 3.5 7 5 5 5" fill="none" stroke="#0e7a3c" stroke-width=".9"/></svg></div><div class="benefit-en">NATURAL INGREDIENTS</div><div class="benefit-bg">НАТУРАЛНИ СЪСТАВКИ</div></div>
  </div>
  <footer class="footer-bar"><span><b>DIETARY SUPPLEMENT</b> | ХРАНИТЕЛНА ДОБАВКА</span><span><b>60 CAPSULES</b> | КАПСУЛИ</span></footer>
</section>

<section class="back-label" style="left:858px">
  <div class="back-block" style="top:8px;height:34px">
    <h3 class="back-heading">COMPOSITION:</h3>
    <p class="back-text">Chios mastica (Pistacia lentiscus L., gum-resin; carrier: corn maltodextrin); capsule (hydroxypropylmethylcellulose); licorice deglycyrrhizinated d.e. 1:4 (Glycyrrhiza glabra L., radix); aloe vera gel 200:1; N-acetylcysteine; red elm d.e. 10:1; althaea d.e. 1:4; lactoferrin 95% (milk); anticaking agent: silicon dioxide.</p>
  </div>
  <div class="back-block" style="top:45px;height:36px">
    <h3 class="back-heading">СЪСТАВ:</h3>
    <p class="back-text">Мастика от Хиос (Pistacia lentiscus L., гума смола; носител: царевичен малтодекстрин); капсула (хидроксипропилметилцелулоза); деглициризирано женско биле с.е. 1:4; гел от алое вера 200:1; N-ацетилцистеин; червен бряст с.е. 10:1; алтея с.е. 1:4; лактоферин 95% (мляко); агент против слепване: силициев диоксид.</p>
  </div>
  <div class="compo-table">
    <div class="th">COMPONENTS<br>СЪСТАВКИ</div><div class="th num">PER 1 CPS<br>ЗА 1 капсула</div><div class="th num">PER 3 CPS<br>За 3 капсули</div>
    <div>Chios Mastica<br>Мастика от Хиос</div><div class="num">320 mg<br>320 мг</div><div class="num">960 mg<br>960 мг</div>
    <div>Licorice deglycyrrhizinated d.e<br>Женско биле с.е.</div><div class="num">80 mg<br>80 мг</div><div class="num">240 mg<br>240 мг</div>
    <div>Aloe vera d.e.<br>Алое вера с.е.</div><div class="num">50 mg<br>50 мг</div><div class="num">150 mg<br>150 мг</div>
    <div>N-acetylcysteine<br>N-ацетилцистеин</div><div class="num">40 mg<br>40 мг</div><div class="num">120 mg<br>120 мг</div>
    <div>Red elm d.e.<br>Червен бряст с.е.</div><div class="num">40 mg<br>40 мг</div><div class="num">120 mg<br>120 мг</div>
    <div>Althaea d.e.<br>Алтея с.е.</div><div class="num">40 mg<br>40 мг</div><div class="num">120 mg<br>120 мг</div>
    <div>Lactoferrin<br>Лактоферин</div><div class="num">30 mg<br>30 мг</div><div class="num">90 mg<br>90 мг</div>
  </div>
  <div class="back-block two-col" style="top:216px;height:20px">
    <div><h3 class="back-heading small">PHYSIOLOGICAL VALUES:</h3><p class="back-text tight">Pistacia lentiscus and Licorice supports digestive system function.</p></div>
    <div><h3 class="back-heading small">ФИЗИОЛОГИЧНИ СТОЙНОСТИ:</h3><p class="back-text tight">Мастиката и женското биле подпомагат функцията на храносмилателната система.</p></div>
  </div>
  <div class="dosage-band"><b>RECOMMENDED DAILY DOSAGE:</b> It is recommended to take up to three capsules per day.<br><b>ПРЕПОРЪЧИТЕЛНА ДНЕВНА ДОЗА:</b> Препоръчва се прием до три капсули на ден.</div>
  <div class="back-block" style="top:255px;height:26px">
    <h3 class="back-heading small">STORAGE CONDITIONS:</h3>
    <p class="back-text tight">Store in a cool, dry place away from light and heat. Keep out of reach of children. Not a substitute for a varied diet. Do not exceed the daily dose. Not for pregnant or nursing women without medical advice.</p>
  </div>
  <div class="back-block" style="top:282px;height:30px">
    <h3 class="back-heading small">УСЛОВИЯ НА СЪХРАНЕНИЕ:</h3>
    <p class="back-text tight">Да се съхранява на сухо и хладно място, далеч от светлина. Да не се оставя на достъпни за деца места. Не е заместител на разнообразното хранене. Да не се превишава дневната доза.</p>
  </div>
  <div class="back-block two-col" style="top:312px;height:12px">
    <div><h3 class="back-heading small">MANUFACTURER/ПРОИЗВОДИТЕЛ:</h3><p class="back-text tight">Aurelia Labs – Via Serena 12, Lecce, Italy</p></div>
    <div><h3 class="back-heading small">DISTRIBUTOR/ДИСТРИБУТОР:</h3><p class="back-text tight">Stolica Trade – ул. Липа 8, Пловдив</p></div>
  </div>
  <div class="lot-band"><span>Lotto: Партида:</span><span>Scadenza:Срок на годност:</span></div>
</section>

<section class="back-label" style="left:1028px">
  <div class="back-block" style="top:8px;height:34px">
    <h3 class="back-heading">COMPOSITION:</h3>
    <p class="back-text">Chios mastica (Pistacia lentiscus L., gum-resin; carrier: corn maltodextrin); capsule (hydroxypropylmethylcellulose); licorice deglycyrrhizinated d.e. 1:4 (Glycyrrhiza glabra L., radix); aloe vera gel 200:1; N-acetylcysteine; red elm d.e. 10:1; althaea d.e. 1:4; lactoferrin 95% (milk); anticaking agent: silicon dioxide.</p>
  </div>
  <div class="back-block" style="top:45px;height:36px">
    <h3 class="back-heading">СЪСТАВ:</h3>
    <p class="back-text">Мастика от Хиос (Pistacia lentiscus L., гума смола; носител: царевичен малтодекстрин); капсула (хидроксипропилметилцелулоза); деглициризирано женско биле с.е. 1:4; гел от алое вера 200:1; N-ацетилцистеин; червен бряст с.е. 10:1; алтея с.е. 1:4; лактоферин 95% (мляко); агент против слепване: силициев диоксид.</p>
  </div>
  <div class="compo-table">
    <div class="th">COMPONENTS<br>СЪСТАВКИ</div><div class="th num">PER 1 CPS<br>ЗА 1 капсула</div><div class="th num">PER 3 CPS<br>За 3 капсули</div>
    <div>Chios Mastica<br>Мастика от Хиос</div><div class="num">320 mg<br>320 мг</div><div class="num">960 mg<br>960 мг</div>
    <div>Licorice deglycyrrhizinated d.e<br>Женско биле с.е.</div><div class="num">80 mg<br>80 мг</div><div class="num">240 mg<br>240 мг</div>
    <div>Aloe vera d.e.<br>Алое вера с.е.</div><div class="num">50 mg<br>50 мг</div><div class="num">150 mg<br>150 мг</div>
    <div>N-acetylcysteine<br>N-ацетилцистеин</div><div class="num">40 mg<br>40 мг</div><div class="num">120 mg<br>120 мг</div>
    <div>Red elm d.e.<br>Червен бряст с.е.</div><div class="num">40 mg<br>40 мг</div><div class="num">120 mg<br>120 мг</div>
    <div>Althaea d.e.<br>Алтея с.е.</div><div class="num">40 mg<br>40 мг</div><div class="num">120 mg<br>120 мг</div>
    <div>Lactoferrin<br>Лактоферин</div><div class="num">30 mg<br>30 мг</div><div class="num">90 mg<br>90 мг</div>
  </div>
  <div class="back-block two-col" style="top:216px;height:20px">
    <div><h3 class="back-heading small">PHYSIOLOGICAL VALUES:</h3><p class="back-text tight">Pistacia lentiscus and Licorice supports digestive system function.</p></div>
    <div><h3 class="back-heading small">ФИЗИОЛОГИЧНИ СТОЙНОСТИ:</h3><p class="back-text tight">Мастиката и женското биле подпомагат функцията на храносмилателната система.</p></div>
  </div>
  <div class="dosage-band"><b>RECOMMENDED DAILY DOSAGE:</b> It is recommended to take up to three capsules per day.<br><b>ПРЕПОРЪЧИТЕЛНА ДНЕВНА ДОЗА:</b> Препоръчва се прием до три капсули на ден.</div>
  <div class="back-block" style="top:255px;height:26px">
    <h3 class="back-heading small">STORAGE CONDITIONS:</h3>
    <p class="back-text tight">Store in a cool, dry place away from light and heat. Keep out of reach of children. Not a substitute for a varied diet. Do not exceed the daily dose. Not for pregnant or nursing women without medical advice.</p>
  </div>
  <div class="back-block" style="top:282px;height:30px">
    <h3 class="back-heading small">УСЛОВИЯ НА СЪХРАНЕНИЕ:</h3>
    <p class="back-text tight">Да се съхранява на сухо и хладно място, далеч от светлина. Да не се оставя на достъпни за деца места. Не е заместител на разнообразното хранене. Да не се превишава дневната доза.</p>
  </div>
  <div class="back-block two-col" style="top:312px;height:12px">
    <div><h3 class="back-heading small">MANUFACTURER/ПРОИЗВОДИТЕЛ:</h3><p class="back-text tight">Aurelia Labs – Via Serena 12, Lecce, Italy</p></div>
    <div><h3 class="back-heading small">DISTRIBUTOR/ДИСТРИБУТОР:</h3><p class="back-text tight">Stolica Trade – ул. Липа 8, Пловдив</p></div>
  </div>
  <div class="lot-band"><span>Lotto: Партида:</span><span>Scadenza:Срок на годност:</span></div>
</section>

</main>
</body>
</html>
```